Media Browser and player web application

I need to redesign a web application that enables to browse a media server (Tellavo) contents (images, audio, video) and play it in a web player.

Current implementation of the application can be seen at: http://www.tellavohub.example/content/demonstration-tellavo-pro-online-media-browser

This refresh is aiming to:
1) make the application simpler, based on typology (think Windows Metro style, VidSpire, Flickora); a simple fan concept is here: http://dex.lomarquin.example/tellavo/
2) make the application work on desktop as well as touch screen devices (ie no hover functionality, no pagination, large touch controls)
3) fast (remove unnecessary animations)
4) design with the app being responsive in mind

The attached UX designs show the basic flows in the application. Please note that the placement of controls (for example) is not set in stone and I welcome your input on the layout.

Ideally the default theme will be dark. Items' thumbnails will be square place holders, with images fit in them depending on the item icons' aspect ratio.

Also attaching the product's logo (Tellavo) and icon. The web application's name is ClipRover (or Tellavo ClipRover), so it should be included in the design (the UX designs include place holder Tellavo logo in the left top corner).

The main categories for each file type are (you will have to provide an icon for each of these):
- Audio: Albums, Artists, Album artists, Folders, Genres, Composers, Titles, Random music, Random albums, Last listened, Playlists, Online
- Image: Albums, Folders, Year, Month, Playlists, Online
- Video: Titles, Movies, Series, Folders, Last viewed, Last added, Genres, Actors, Directors, Producers, Release years, Playlists, Online
Updates

Target Market(s)

Mostly tech enthusiasts who want to stream their media over the internet to their devices.

Industry/Entity Type

Artists

Requirements
Must have
• Designs for all the provided UX designs
Touch-friendly web application design
High-res (Retina) assets
Light, type based Metro-like design
Nice to have
• Responsive web version
Dark and Light theme switching.
Should not have
• Chrome
Heavy graphics (eg backgrounds) that take time to load

```html
<!DOCTYPE html>
<html lang="en">
<head>
<meta charset="utf-8">
<title>Tellavo ClipRover – Audio</title>
<link href="https://fonts.googleapis.com/css2?family=Questrial&display=swap" rel="stylesheet">
<style>
  :root {
    --bg: #0c0c0c;
    --yellow: #f5e400;
    --olive: #a89d14;
    --grey: #9a9a9a;
    --tile-grey: #5f5f5f;
    --white: #ffffff;
  }
  * { margin: 0; padding: 0; box-sizing: border-box; }
  html, body { width: 1200px; height: 647px; overflow: hidden; background: var(--bg); }
  body { font-family: "Questrial", "Century Gothic", sans-serif; color: var(--white); position: relative; }

  .defs { position: absolute; width: 0; height: 0; }

  .brand { position: absolute; left: 213px; top: 63px; display: flex; align-items: center; gap: 10px; }
  .brand-mark { width: 40px; height: 40px; background: var(--yellow); border-radius: 5px; }
  .brand-name { font-size: 44px; line-height: 1; color: var(--white); letter-spacing: 1px; }

  .user { position: absolute; top: 65px; left: 723px; display: flex; align-items: center; }
  .user-avatar { width: 39px; height: 39px; border: 2px solid var(--yellow); background: linear-gradient(160deg, #8a8a8a, #2b2b2b); }
  .user-welcome { margin-left: 26px; font-size: 14px; color: var(--grey); }
  .user-name { color: var(--olive); }
  .sign-out { margin-left: 26px; font-size: 14px; color: var(--olive); display: flex; align-items: center; gap: 4px; text-decoration: none; margin-top: -3px; }

  .breadcrumb { position: absolute; left: 208px; top: 160px; display: flex; align-items: center; font-size: 14px; color: var(--grey); letter-spacing: 0.3px; }
  .breadcrumb .sep { margin: 0 4px 0 10px; }
  .breadcrumb .current { color: var(--olive); }

  .toolbar { position: absolute; left: 959px; top: 153px; display: flex; gap: 6px; }
  .tool { width: 31px; height: 30px; display: flex; align-items: center; justify-content: center; }
  .tool-menu { background: var(--yellow); }
  .tool-search { background: var(--tile-grey); }

  .category { position: absolute; width: 130px; height: 110px; text-decoration: none; }
  .category-icon { position: absolute; left: 0; top: 0; width: 112px; height: 76px; overflow: visible; }
  .category-label { position: absolute; top: 84px; font-size: 13.5px; color: var(--white); white-space: nowrap; }
</style>
</head>
<body>

<svg class="defs" aria-hidden="true">
  <defs>
    <linearGradient id="folderFront" x1="0" y1="0" x2="0" y2="1">
      <stop offset="0" stop-color="#fff48a"/>
      <stop offset="0.55" stop-color="#f5dc10"/>
      <stop offset="1" stop-color="#e0a800"/>
    </linearGradient>
    <linearGradient id="silver" x1="0" y1="0" x2="1" y2="1">
      <stop offset="0" stop-color="#f2f2f2"/>
      <stop offset="1" stop-color="#8c8c8c"/>
    </linearGradient>
    <linearGradient id="darkDisc" x1="0" y1="0" x2="0" y2="1">
      <stop offset="0" stop-color="#3a3a3a"/>
      <stop offset="1" stop-color="#0a0a0a"/>
    </linearGradient>
    <symbol id="folder" viewBox="0 0 90 72">
      <path d="M2 6 Q2 2 6 2 H30 L35 7 H84 Q88 7 88 11 V60 H2 Z" fill="#c79600"/>
      <rect x="8" y="10" width="74" height="7" fill="#f4f4f4"/>
      <path d="M0 18 Q0 15 3 15 H87 Q90 15 90 18 L87 68 Q86 72 82 72 H8 Q4 72 3 68 Z" fill="url(#folderFront)"/>
    </symbol>
  </defs>
</svg>

<header>
  <div class="brand">
    <span class="brand-mark"></span>
    <span class="brand-name">Tellavo</span>
  </div>

  <div class="user">
    <div class="user-avatar" role="img" aria-label="User profile photo"></div>
    <span class="user-welcome">Welcome, <span class="user-name">Dale Harper</span></span>
    <a class="sign-out" href="#">
      <svg width="16" height="14" viewBox="0 0 16 14" aria-hidden="true">
        <circle cx="7" cy="7" r="5" fill="none" stroke="#f5e400" stroke-width="2.4"/>
        <path d="M6 7h9M12 4l3 3-3 3" fill="none" stroke="#f5e400" stroke-width="2.2"/>
      </svg>
      Sign Out
    </a>
  </div>
</header>

<nav class="breadcrumb">
  <svg width="22" height="21" viewBox="0 0 22 21" aria-label="Home">
    <path d="M11 1L1 10h3v10h5v-6h4v6h5V10h3z" fill="#f5e400"/>
  </svg>
  <span class="sep">»</span><span>AUDIO</span>
  <span class="sep">»</span><span class="current">My Personal Collection</span>
</nav>

<div class="toolbar">
  <a class="tool tool-menu" href="#" aria-label="Menu">
    <svg width="22" height="18" viewBox="0 0 22 18"><path d="M0 2h22M0 9h22M0 16h22" stroke="#111" stroke-width="3.2"/></svg>
  </a>
  <a class="tool tool-search" href="#" aria-label="Search">
    <svg width="22" height="22" viewBox="0 0 22 22"><circle cx="8.5" cy="8.5" r="6.5" fill="none" stroke="#fff" stroke-width="2"/><path d="M13 13l7 7" stroke="#fff" stroke-width="3"/></svg>
  </a>
</div>

<main class="categories">
  <a class="category" href="#" style="left:202px;top:230px">
    <svg class="category-icon" viewBox="0 0 112 76" aria-label="Artists folder">
      <use href="#folder" x="0" y="2" width="90" height="72"/>
      <rect x="66" y="1" width="22" height="34" rx="11" fill="url(#silver)"/>
      <path d="M66 12h22M66 18h22M66 24h22" stroke="#777" stroke-width="1"/>
      <rect x="68" y="30" width="18" height="16" rx="4" fill="#151515"/>
      <path d="M62 30 Q62 50 77 50 Q92 50 92 30" fill="none" stroke="#bbb" stroke-width="2"/>
      <path d="M77 50v16M66 70h22" stroke="#bbb" stroke-width="2.5"/>
    </svg>
    <span class="category-label" style="left:6px">Artists</span>
  </a>

  <a class="category" href="#" style="left:348px;top:230px">
    <svg class="category-icon" viewBox="0 0 112 76" aria-label="Album Artists folder">
      <use href="#folder" x="0" y="2" width="90" height="72"/>
      <circle cx="70" cy="38" r="35" fill="#111"/>
      <circle cx="70" cy="38" r="28" fill="none" stroke="#2e2e2e" stroke-width="1"/>
      <circle cx="70" cy="38" r="21" fill="none" stroke="#2e2e2e" stroke-width="1"/>
      <circle cx="70" cy="38" r="10" fill="#e2e2e2"/>
      <circle cx="70" cy="38" r="1.5" fill="#333"/>
    </svg>
    <span class="category-label" style="left:3px">Album Artists</span>
  </a>

  <a class="category" href="#" style="left:494px;top:230px">
    <svg class="category-icon" viewBox="0 0 112 76" aria-label="Folders folder">
      <use href="#folder" x="0" y="2" width="90" height="72"/>
    </svg>
    <span class="category-label" style="left:12px">Folders</span>
  </a>

  <a class="category" href="#" style="left:639px;top:230px">
    <svg class="category-icon" viewBox="0 0 112 76" aria-label="Genres folder">
      <use href="#folder" x="0" y="2" width="90" height="72"/>
      <circle cx="72" cy="42" r="34" fill="url(#silver)"/>
      <path d="M62 52V24l30-7v29" fill="none" stroke="#111" stroke-width="4"/>
      <ellipse cx="58" cy="53" rx="7" ry="5.5" fill="#111"/>
      <ellipse cx="88" cy="47" rx="7" ry="5.5" fill="#111"/>
    </svg>
    <span class="category-label" style="left:11px">Genres</span>
  </a>

  <a class="category" href="#" style="left:786px;top:230px">
    <svg class="category-icon" viewBox="0 0 112 76" aria-label="Composers folder">
      <use href="#folder" x="0" y="2" width="90" height="72"/>
      <rect x="47" y="1" width="63" height="68" fill="#2a2a2a"/>
      <circle cx="78" cy="35" r="28" fill="url(#silver)"/>
      <circle cx="78" cy="35" r="9" fill="#bdbdbd" stroke="#888"/>
      <circle cx="78" cy="35" r="4" fill="#2a2a2a"/>
    </svg>
    <span class="category-label" style="left:6px">Composers</span>
  </a>

  <a class="category" href="#" style="left:202px;top:377px">
    <svg class="category-icon" viewBox="0 0 112 76" aria-label="Titles folder">
      <use href="#folder" x="0" y="2" width="90" height="72"/>
      <path d="M58 60V12l32-8v46" fill="none" stroke="#151515" stroke-width="5"/>
      <path d="M58 12l32-8v12l-32 8z" fill="#151515"/>
      <ellipse cx="51" cy="61" rx="9" ry="7" fill="#151515"/>
      <ellipse cx="83" cy="52" rx="9" ry="7" fill="#151515"/>
    </svg>
    <span class="category-label" style="left:6px">Titles</span>
  </a>

  <a class="category" href="#" style="left:348px;top:377px">
    <svg class="category-icon" viewBox="0 0 112 76" aria-label="Random folder">
      <use href="#folder" x="0" y="2" width="90" height="72"/>
      <circle cx="71" cy="40" r="34" fill="url(#darkDisc)" stroke="#555" stroke-width="1.5"/>
      <path d="M71 40 C63 30 50 30 50 40 C50 50 63 50 71 40 C79 30 92 30 92 40 C92 50 79 50 71 40Z" fill="none" stroke="#d8d8d8" stroke-width="5"/>
    </svg>
    <span class="category-label" style="left:4px">Random</span>
  </a>

  <a class="category" href="#" style="left:494px;top:377px">
    <svg class="category-icon" viewBox="0 0 112 76" aria-label="Playlists folder">
      <use href="#folder" x="0" y="2" width="90" height="72"/>
      <circle cx="75" cy="40" r="33" fill="url(#darkDisc)" stroke="#d0d0d0" stroke-width="2"/>
      <path d="M66 26v28l25-14z" fill="#e8e8e8"/>
    </svg>
    <span class="category-label" style="left:12px">Playlists</span>
  </a>

  <a class="category" href="#" style="left:639px;top:377px">
    <svg class="category-icon" viewBox="0 0 112 76" aria-label="Online folder">
      <use href="#folder" x="0" y="2" width="90" height="72"/>
      <circle cx="75" cy="40" r="34" fill="url(#silver)"/>
      <g fill="none" stroke="#555" stroke-width="1.2">
        <ellipse cx="75" cy="40" rx="14" ry="34"/>
        <ellipse cx="75" cy="40" rx="27" ry="34"/>
        <path d="M75 6v68M41 40h68M45 24h60M45 56h60"/>
      </g>
    </svg>
    <span class="category-label" style="left:11px">Online</span>
  </a>
</main>

</body>
</html>
```